Taking Steps; Garden Table, Bright Days Rack Card

We want an additional 2 page (front and page) 3.67" x 8.5" rack card. This rack card is now the 2nd of the series . The first one is already completed/finalized and attached (Garden Table Bright Days Rack Card PDF).
Use the text on the word document for the included Taking Steps Rack card. Please use the Garden Table Bright Days Rack card as the template to mimic. We would like all subsequent rack cards to have a similar look and feel.
The document is for older readers. Do not put text over graphics and keep it simple and easy to read with high contrast.
We want some very simple design element(s) incorporated that convey Native American communities or heritage. But NO headdress, teepee graphics, etc. At the top, of the first page we would like a collage of healthy food images. This can include fish, chicken, fresh vegetables, berries, brown rice, etc. Please remember to include the funding statement - it can be in a very small font 6/7 point. For more information about our project, please visit https://plovanta.org/elder-wellness/

```html
<!DOCTYPE html>
<html lang="en">
<head>
<meta charset="utf-8">
<title>Taking Steps; Garden Table, Bright Days Rack Card</title>
<link rel="stylesheet" href="https://fonts.googleapis.com/css2?family=Montserrat:wght@400;500;600;700;800&display=swap">
<style>
  :root {
    --maroon: #5a1c1c;
    --teal: #4aafb3;
    --teal-deep: #2f8a8c;
    --teal-ink: #174a52;
    --coral: #c2574a;
    --ink: #2b2b2b;
    --paper: #f7f7f5;
    --stage: #8c8c8c;
    --white: #ffffff;
  }
  * { box-sizing: border-box; margin: 0; padding: 0; }
  html, body { width: 1200px; height: 1200px; overflow: hidden; }
  body {
    background: var(--stage);
    font-family: "Montserrat", sans-serif;
    color: var(--ink);
    position: relative;
  }
  .card {
    position: absolute;
    top: 74px;
    width: 454px;
    height: 1050px;
    background: var(--paper);
    overflow: hidden;
  }
  .card--front { left: 111px; }
  .card--back { left: 634px; }
  .abs { position: absolute; }

  /* front */
  .food-collage {
    left: 0; top: 0; width: 454px; height: 140px;
    background: linear-gradient(90deg, #c98a3a 0%, #d9a25a 25%, #e2503a 45%, #7fae3f 55%, #e8d7b0 75%, #5b8a92 100%);
  }
  .title { left: 24px; top: 150px; width: 420px; }
  .title__line {
    display: block; font-weight: 800; font-size: 48px; line-height: 45px;
    letter-spacing: 0.3px; white-space: nowrap;
  }
  .title__line--maroon { color: var(--maroon); }
  .title__line--teal { color: var(--teal); }
  .title__line--thin { font-weight: 400; color: var(--maroon); font-size: 46px; }
  .intro { left: 24px; top: 292px; width: 410px; font-size: 12.3px; font-weight: 500; line-height: 1.2; }
  .subhead { left: 24px; top: 350px; font-size: 17px; font-weight: 700; color: var(--teal-ink); }
  .subhead em { font-style: normal; color: var(--coral); }
  .checklist { left: 24px; top: 385px; width: 414px; list-style: none; }
  .checklist li {
    display: flex; gap: 10px; font-size: 12.3px; line-height: 1.2; margin-bottom: 13px;
  }
  .checklist svg { flex: 0 0 12px; width: 12px; height: 12px; margin-top: 1px; }
  .checklist .quote-accent { color: var(--teal); font-style: italic; }
  .chevron-band {
    left: 0; width: 454px; height: 23px;
    background: linear-gradient(90deg, var(--teal) 0%, var(--coral) 50%, var(--teal) 100%);
    opacity: 0.75;
  }
  .doctor-band {
    left: 0; top: 708px; width: 454px; height: 58px; background: var(--maroon);
    color: var(--white); font-weight: 700; font-size: 12.6px; line-height: 1.5;
    padding: 9px 24px 0;
  }
  .quote { left: 24px; top: 773px; width: 230px; }
  .quote__mark { font-size: 42px; font-weight: 800; color: var(--teal); line-height: 0.8; height: 24px; }
  .quote__text { font-weight: 700; font-size: 15px; line-height: 1.25; color: var(--ink); margin-top: 6px; }
  .quote__text span { color: var(--teal); font-size: 30px; line-height: 0; vertical-align: -8px; }
  .quote__cite { font-size: 10px; margin-top: 10px; }
  .berry-basket {
    left: 262px; top: 772px; width: 182px; height: 142px; border-radius: 8px;
    background: radial-gradient(circle at 50% 55%, #b0412e 0%, #a4703e 40%, #f2f2f0 75%);
  }
  .footer {
    left: 0; top: 939px; width: 454px; height: 111px; background: var(--teal-deep);
    color: var(--white); font-size: 9.6px; line-height: 1.3; padding: 18px 26px 0;
  }

  /* back */
  .home-title { left: 23px; top: 55px; font-weight: 800; font-size: 37px; color: var(--maroon); white-space: nowrap; }
  .home-title span { color: var(--teal); }
  .recipe-name { left: 25px; top: 106px; font-weight: 700; font-size: 13.5px; color: var(--teal-ink); }
  .stew-photo {
    left: 25px; top: 137px; width: 165px; height: 131px;
    background: radial-gradient(circle at 50% 45%, #d9c8a0 0%, #8a5a33 45%, #6e5e4c 100%);
  }
  .ingredients { left: 206px; top: 144px; width: 220px; }
  .ingredients h3 { font-size: 14px; font-weight: 700; margin-bottom: 10px; }
  .ingredients p { font-size: 11.6px; line-height: 1.25; }
  .method { left: 25px; top: 285px; width: 408px; font-size: 11.6px; line-height: 1.25; }
  .elders-band {
    left: 0; top: 406px; width: 454px; height: 190px; background: var(--maroon);
    color: var(--white); font-weight: 800; font-size: 19.6px; line-height: 1.27;
    padding: 22px 24px 0 30px; text-transform: uppercase;
  }
  .more-info { left: 0; top: 640px; width: 454px; text-align: center; }
  .more-info h2 { font-weight: 800; font-size: 23px; color: var(--maroon); }
  .more-info h2 span { color: var(--teal); }
  .more-info h3 { font-weight: 500; font-size: 20px; color: var(--ink); margin-top: 6px; }
  .resource { font-size: 13.5px; font-weight: 500; color: var(--coral); margin-top: 10px; }
  .link-pill {
    display: block; width: 304px; height: 26px; margin: 5px auto 0; border-radius: 13px;
    background: var(--teal); color: var(--white); font-weight: 600; font-size: 13.3px; line-height: 26px;
  }
  .org-mark { left: 0; top: 846px; width: 454px; display: flex; justify-content: center; align-items: center; gap: 10px; }
  .org-mark__dot { width: 40px; height: 40px; border-radius: 50%; background: var(--teal); }
  .org-mark__name { font-weight: 700; font-size: 15px; color: var(--teal); line-height: 1.1; }
</style>
</head>
<body>

<article class="card card--front">
  <div class="abs food-collage" role="img" aria-label="Collage of healthy foods: roast chicken with salad, colourful tomatoes, brown rice with grilled vegetables"></div>

  <h1 class="abs title">
    <span class="title__line title__line--maroon">GARDEN TABLE</span>
    <span class="title__line title__line--teal">BRIGHT DAYS</span>
    <span class="title__line title__line--thin">TAKING STEPS</span>
  </h1>

  <p class="abs intro">Making small changes in what and how you eat can make you feel better and stay healthier longer. Healthy food choices may be good for your brain, energy, mood, and health.</p>

  <h2 class="abs subhead">Little changes that make a <em>big difference:</em></h2>

  <ul class="abs checklist">
    <li><svg viewBox="0 0 12 12"><rect x="0.6" y="1.6" width="9.8" height="9.8" fill="none" stroke="#c2574a" stroke-width="1.2"/><path d="M2.8 6.2 5.2 8.6 11.4 1" fill="none" stroke="#c2574a" stroke-width="1.4"/></svg><span>Start today!</span></li>
    <li><svg viewBox="0 0 12 12"><rect x="0.6" y="1.6" width="9.8" height="9.8" fill="none" stroke="#c2574a" stroke-width="1.2"/><path d="M2.8 6.2 5.2 8.6 11.4 1" fill="none" stroke="#c2574a" stroke-width="1.4"/></svg><span>Write down what, when, and how much you eat for three days</span></li>
    <li><svg viewBox="0 0 12 12"><rect x="0.6" y="1.6" width="9.8" height="9.8" fill="none" stroke="#c2574a" stroke-width="1.2"/><path d="M2.8 6.2 5.2 8.6 11.4 1" fill="none" stroke="#c2574a" stroke-width="1.4"/></svg><span>Set SMART goals (Specific, Measurable, Attainable, Relevant &amp; Timebound), like: “I will eat one piece of fruit at breakfast three times this week.”</span></li>
    <li><svg viewBox="0 0 12 12"><rect x="0.6" y="1.6" width="9.8" height="9.8" fill="none" stroke="#c2574a" stroke-width="1.2"/><path d="M2.8 6.2 5.2 8.6 11.4 1" fill="none" stroke="#c2574a" stroke-width="1.4"/></svg><span>Make just 1 or 2 changes at a time until they become a habit</span></li>
    <li><svg viewBox="0 0 12 12"><rect x="0.6" y="1.6" width="9.8" height="9.8" fill="none" stroke="#c2574a" stroke-width="1.2"/><path d="M2.8 6.2 5.2 8.6 11.4 1" fill="none" stroke="#c2574a" stroke-width="1.4"/></svg><span>Focus more on eating healthy food versus not eating unhealthy food</span></li>
    <li><svg viewBox="0 0 12 12"><rect x="0.6" y="1.6" width="9.8" height="9.8" fill="none" stroke="#c2574a" stroke-width="1.2"/><path d="M2.8 6.2 5.2 8.6 11.4 1" fill="none" stroke="#c2574a" stroke-width="1.4"/></svg><span>Make a game plan for the times you get tempted to eat unhealthy foods</span></li>
    <li><svg viewBox="0 0 12 12"><rect x="0.6" y="1.6" width="9.8" height="9.8" fill="none" stroke="#c2574a" stroke-width="1.2"/><path d="M2.8 6.2 5.2 8.6 11.4 1" fill="none" stroke="#c2574a" stroke-width="1.4"/></svg><span>Involve the whole family in setting goals</span></li>
    <li><svg viewBox="0 0 12 12"><rect x="0.6" y="1.6" width="9.8" height="9.8" fill="none" stroke="#c2574a" stroke-width="1.2"/><path d="M2.8 6.2 5.2 8.6 11.4 1" fill="none" stroke="#c2574a" stroke-width="1.4"/></svg><span>Name your main reason to eat healthier and feel better, like <span class="quote-accent">“More energy to go to church and tribal cultural events.”</span></span></li>
  </ul>

  <div class="abs chevron-band" style="top:685px" role="img" aria-label="Zigzag chevron border in teal and coral"></div>

  <p class="abs doctor-band">TALK TO YOUR DOCTOR ABOUT HEALTHIER EATING TO MAKE YOU FEEL BETTER AND STAY HEALTHIER LONGER.</p>

  <blockquote class="abs quote">
    <div class="quote__mark">“</div>
    <p class="quote__text">When it comes to traditional foods, for me it’s something more than just food, it’s my heritage. <span>”</span></p>
    <p class="quote__cite">Delora Manu (Red Mesa Nation)</p>
  </blockquote>

  <div class="abs berry-basket" role="img" aria-label="Wicker basket filled with fresh berries and cherries"></div>

  <div class="abs chevron-band" style="top:917px" role="img" aria-label="Zigzag chevron border in teal and coral"></div>

  <p class="abs footer">This product is supported by the National Wellness Fund (NWF) of the Office of Community Health (OCH) as part of a financial assistance award totaling $348,711 with 100 percent funded by NWF/OCH. The contents are those of the author(s) and do not necessarily represent the official views of, nor an endorsement, by NWF/OCH, or the Regional Government.</p>
</article>

<article class="card card--back">
  <h2 class="abs home-title">MAKE THIS <span>AT HOME</span></h2>
  <h3 class="abs recipe-name">O’odham White Tepary Bean Stew</h3>

  <div class="abs stew-photo" role="img" aria-label="Wooden bowl of white tepary bean stew with meat"></div>

  <div class="abs ingredients">
    <h3>Ingredients:</h3>
    <p>1 cup dried tepary beans, rinsed &amp; picked through (substitute Navy Beans or Great Northern beans), 10 cups of water, 1 tsp. salt, 1 lb. oxtails, beef short ribs, deer, rabbit, or chicken</p>
  </div>

  <p class="abs method">Put beans, water, and salt in a stockpot. Bring to a boil, reduce heat and simmer, covered, for one hour and a half. Add meat to the bean mixture, cover and cook for one more hour, or until beans are tender and meat is falling off the bone. If using a crockpot, place water and all other ingredients in the pot, cover, and set to high. Cook for 8 hours or until the meat is falling off the bone and the beans are tender.</p>

  <p class="abs elders-band">Elders are our keepers of traditional knowledge about food and ways of life. You play an important role in sharing this knowledge with younger generations.</p>

  <div class="abs chevron-band" style="top:596px" role="img" aria-label="Zigzag chevron border in teal and coral"></div>

  <section class="abs more-info">
    <h2>FOR MORE <span>INFORMATION</span></h2>
    <h3>About Goal Setting</h3>
    <p class="resource">Council for Nourished Living</p>
    <span class="link-pill">https://bit.ly/NourishGoalSettingVideo</span>
    <p class="resource">Harlow Bay Medicine</p>
    <span class="link-pill">https://bit.ly/HBMSmartGoals</span>
  </section>

  <div class="abs org-mark">
    <span class="org-mark__dot"></span>
    <span class="org-mark__name">PLOVANTA ELDER<br>WELLNESS CENTER</span>
  </div>

  <div class="abs chevron-band" style="top:916px" role="img" aria-label="Zigzag chevron border in teal and coral"></div>

  <p class="abs footer">This product is supported by the National Wellness Fund (NWF) of the Office of Community Health (OCH) as part of a financial assistance award totaling $348,711 with 100 percent funded by NWF/OCH. The contents are those of the author(s) and do not necessarily represent the official views of, nor an endorsement, by NWF/OCH, or the Regional Government.</p>
</article>

</body>
</html>
```